Flyer Design

The company nane is "KELDA RUNN GROUNDWORKS" it is a earthmoving company using a skid steer or wombix with tracks, the type of work I will be doing range from site cleans, pavings preps, house pads, final trim, landscaping, pool digs. Call 0462735018

i have posted a foto of the new design for the logo, please incorporate somehow, also i am using a velmor dura glide kx40 skid steer, i am not using a front end loader or digger or anu other earthmoving gear so dont use them.

include easy narrow access

Very experienced in all aspects of wombix work. Rubbish removal. House and shed pads. Paving prep Concrete removal. Lawn removal. Clearing Limestone driveways. Limestone block lifting. Levelling.

If you want it done fast. Wether your after site cleans, paving preps, earth moving, house pads, final trim or yard demos we cater for the lot. Our specialty equipment can do the lot

I have uploaded 2 new pictures, one is the actual logo of the business and the other is the picture I want used on the flyer, think outside the box

```html
<!DOCTYPE html>
<html lang="en">
<head>
<meta charset="utf-8">
<title>Kelda Runn Groundworks Flyer</title>
<link href="https://fonts.googleapis.com/css2?family=Anton&family=Arimo:wght@400;700&display=swap" rel="stylesheet">
<style>
  :root {
    --page-bg: #2a2a2a;
    --ink-dark: #1d1d1d;
    --brand-orange: #e0531d;
    --band-dark: #1f1f20;
    --panel-white: #ffffff;
    --sky-top: #2f86d0;
    --sky-mid: #8cc5ec;
    --sky-low: #dcebf5;
    --machine-yellow: #f2a81c;
    --machine-amber: #d98a12;
    --ground: #8d8781;
    --text-light: #ffffff;
  }
  * { box-sizing: border-box; margin: 0; padding: 0; }
  html, body { width: 1200px; height: 1000px; overflow: hidden; }
  body {
    background: var(--page-bg);
    display: flex; align-items: center; justify-content: center;
  }
  .flyer {
    position: relative;
    width: 960px; height: 660px;
    overflow: hidden;
    background: var(--sky-low);
    box-shadow: 0 10px 30px rgba(0,0,0,.5);
  }
  .hero-photo {
    position: absolute; inset: 0;
    background:
      radial-gradient(ellipse 230px 260px at 730px 300px, rgba(242,168,28,.85) 0%, rgba(217,138,18,.55) 45%, rgba(217,138,18,0) 100%),
      radial-gradient(ellipse 120px 80px at 560px 450px, rgba(150,150,150,.6) 0%, rgba(150,150,150,0) 100%),
      linear-gradient(180deg, transparent 62%, #d6dadb 62%, #d6dadb 68%, var(--ground) 70%, #6f6a64 100%),
      linear-gradient(180deg, var(--sky-top) 0%, var(--sky-mid) 35%, var(--sky-low) 62%);
  }
  .headline {
    position: absolute; left: 46px; top: 44px;
    font-family: "Anton", sans-serif;
    text-transform: uppercase;
    line-height: 1;
  }
  .headline .name-top { display: block; font-size: 66px; color: var(--ink-dark); letter-spacing: 1px; }
  .headline .name-bottom { display: block; font-size: 72px; color: var(--brand-orange); letter-spacing: 1px; margin-top: 4px; }
  .divider {
    position: absolute; left: 46px; top: 210px; width: 420px;
    border-top: 2px dotted #5a6470;
  }
  .services {
    position: absolute; left: 50px; top: 224px;
    display: grid; grid-template-columns: 225px 220px; row-gap: 4px;
    list-style: none;
    font-family: "Arimo", sans-serif; font-size: 26px; color: var(--ink-dark);
  }
  .services li::before { content: "\2022"; margin-right: 10px; }
  .contact-band { position: absolute; left: 0; top: 0; width: 960px; height: 660px; }
  .call {
    position: absolute; left: 46px; bottom: 34px;
    color: var(--text-light);
    display: flex; align-items: baseline; gap: 22px;
  }
  .call .call-label { font-family: "Arimo", sans-serif; font-size: 42px; }
  .call .call-number { font-family: "Anton", sans-serif; font-size: 64px; letter-spacing: 2px; }
  .brand-mark {
    position: absolute; right: 56px; bottom: 62px;
    display: flex; align-items: center; gap: 12px;
    font-family: "Arimo", sans-serif; font-weight: 700; font-size: 26px;
    color: var(--ink-dark); text-transform: uppercase;
    line-height: 1.1;
  }
  .brand-mark .mark-dot { width: 34px; height: 34px; border-radius: 50%; background: var(--brand-orange); flex: none; }
</style>
</head>
<body>
  <div class="flyer">
    <div class="hero-photo" role="img" aria-label="Tracked skid steer loader working on a cleared building site under a blue sky"></div>

    <h1 class="headline">
      <span class="name-top">Kelda Runn</span>
      <span class="name-bottom">Groundworks</span>
    </h1>
    <div class="divider"></div>
    <ul class="services">
      <li>Site Cleans</li><li>Pavings Preps</li>
      <li>House Pads</li><li>Final Trim</li>
      <li>Landscaping</li><li>Pool Digs</li>
    </ul>

    <svg class="contact-band" viewBox="0 0 960 660" aria-hidden="true">
      <polygon points="0,560 560,530 580,660 0,660" fill="var(--band-dark)"/>
      <polygon points="520,532 548,506 556,530" fill="var(--brand-orange)"/>
      <polygon points="545,506 960,478 960,660 580,660" fill="var(--panel-white)"/>
    </svg>

    <div class="call">
      <span class="call-label">Call</span>
      <span class="call-number">0462735018</span>
    </div>

    <div class="brand-mark">
      <span class="mark-dot"></span>
      <span>Kelda Runn<br>Groundworks</span>
    </div>
  </div>
</body>
</html>
```